依頼詳細
既存の看板(居酒屋)がついているのでお昼ラーメンをやっているのがとても分かりづらく新規の集客に困っています。

のぼりをみてお店に入ってもらえるようなデザインをよろしくお願いします。
(HP、インスタを見て頂き、デザインやキャッチコピーはプロの方にお任せ致します)
好き勝手デザインしてくださいm(__)m

■お店の詳細
●HP
https://www.hanabetsu.example/morosuke/
●インスタ
https://www.photogramo.example/morosuke.gyozadon/
記載項目
現在の外観A看板、のぼりの写真張っておきます。
素材でつかう写真も添付しておきます

※同時にA看板のデザインも募集しているのでよろしければそちらもご参加ください。
希望イメージ
シンプル 複雑
単色 カラフル
暗い 明るい
日常 高級
遊び心 厳粛
未来的 伝統的
女性的 男性的
希望する色
納品ファイル
補足説明
のぼりのサイズです。
A看板のデザインも大募集!
https://www.kobodesk.example/work/detail/7192058
期間を延ばしてほしいとの要望がありましたので二日だけ延長致します。
よろしくお願いします。
■ 選んだ理由

バランスが良くみやすかったです。

■ 提案者全員のお礼・コメント

たくさんのご提案ありがとうございました。

```html
<!DOCTYPE html>
<html lang="ja">
<head>
<meta charset="utf-8">
<title>至極のワンタン麺 営業中 のぼり</title>
<link rel="stylesheet" href="https://fonts.googleapis.com/css2?family=Shippori+Mincho+B1:wght@800&family=Yuji+Syuku&display=swap">
<style>
  :root {
    --page: #ffffff;
    --banner: #fffefb;
    --edge: #e4e1dc;
    --ink: #2a2320;
    --red: #c8242c;
    --warm: #f0d27e;
    --cream: #f8ecc8;
    --grey: #dcd8d3;
    --mist: #eeebe6;
  }
  * { margin: 0; padding: 0; box-sizing: border-box; }
  html, body { width: 849px; height: 1200px; overflow: hidden; background: var(--page); }
  .canvas { position: relative; width: 849px; height: 1200px; }
  .banner {
    position: absolute; left: 240px; top: 23px; width: 368px; height: 1152px;
    background: var(--banner); border: 1px solid var(--edge);
    overflow: hidden;
  }
  .illustration {
    position: absolute; left: 0; top: 420px; width: 368px; height: 660px;
    background:
      radial-gradient(ellipse 48% 26% at 52% 76%, #fbf3da 0%, var(--cream) 45%, rgba(248,236,200,0) 100%),
      radial-gradient(ellipse 60% 34% at 50% 74%, var(--warm) 0%, rgba(240,210,126,0.5) 55%, rgba(240,210,126,0) 100%),
      radial-gradient(ellipse 34% 26% at 54% 24%, var(--mist) 0%, var(--grey) 60%, rgba(220,216,211,0) 100%),
      radial-gradient(ellipse 70% 40% at 52% 50%, var(--mist) 0%, rgba(238,235,230,0) 100%);
  }
  .vertical { position: absolute; writing-mode: vertical-rl; white-space: nowrap; z-index: 1; }
  .headline {
    right: 36px; top: 30px;
    font-family: "Yuji Syuku", serif; font-size: 56px; line-height: 1; color: var(--ink);
    letter-spacing: 0.02em;
  }
  .headline .particle { font-size: 40px; }
  .subline {
    right: 118px; top: 135px;
    font-family: "Yuji Syuku", serif; font-size: 34px; line-height: 1; color: var(--ink);
    letter-spacing: 0.08em;
  }
  .open-sign {
    right: 188px; top: 108px;
    font-family: "Shippori Mincho B1", serif; font-weight: 800;
    font-size: 124px; line-height: 1; color: var(--red);
    letter-spacing: 0.04em;
  }
  .shop-name {
    left: 42px; top: 512px;
    font-family: "Yuji Syuku", serif; font-size: 40px; line-height: 1; color: var(--ink);
    letter-spacing: 0.05em;
  }
  .shop-name .mark {
    display: inline-block; width: 14px; height: 14px; margin-top: 10px;
    background: var(--red);
  }
</style>
</head>
<body>
<main class="canvas">
  <section class="banner" aria-label="のぼり">
    <div class="illustration" role="img" aria-label="ワンタン麺の丼を両手で差し出す店主のイラスト"></div>
    <h2 class="vertical headline">至極<span class="particle">の</span>ワンタン麺</h2>
    <p class="vertical subline">心を込めて</p>
    <h1 class="vertical open-sign">営業中</h1>
    <p class="vertical shop-name">もろすけ<span class="mark"></span></p>
  </section>
</main>
</body>
</html>
```